Lumivane, Business Intelligence Consultant Web Design

We need a web design for a Business Intelligence Consultant Enterprise.
We design, develop and mantain management systems and reports that delivered to the final user a complete information about their business. With that information they can take better management decisions.
Our principal service is KRV Business Intelligence proyects, using KRV Stockvault and KRV Quillmark tools.
Also we develop web systems that integrate mobile technology with KRV Systems and end user database systems.

Our principal objective is to be a partner of our clients more than a service provider, the idea is to offer a complete service to our customers that allow both companies grow togheter.

The final design must present our list of services and products, and show our experience in business intelligence projects.

Target Market(s)

Companies that runs KRV systems, Business companies, companies with production processes, retail, logistic process (inventory management)

Industry/Entity Type

Business

Requirements
Must have
• The brochure must have 4 pages:
Home
Empresa
Business Intelligence
Aplicaciones empresariales móviles
Metodología

And a contact form to receive customer contact.
- Name
- Company
- Contact Email
- Message text

For the color I will upload both company logos with different colors that u can use. Obviously you can add color if you want.
Nice to have
• The principal idea is to show to customer that all information of his business can be summarized on one graphic panel and can be consulted from any device.

Is nice to have business graphics on the web design, maybe abstract and give the idea of management information can be obtained easily.

Should not have
• Please, PLEASE!, don't use on the web site a meeting photo or people watching a business report on a lobby or some business man making a presentation.
Neither images of team building or people at the office.

That images are too used to present the business intelligence concept and the principal idea is to have information, and not people working hard to obtain that.

```html
<!DOCTYPE html>
<html lang="es">
<head>
<meta charset="utf-8">
<title>Lumivane – Business Intelligence</title>
<link rel="stylesheet" href="https://fonts.googleapis.com/css2?family=Arimo:wght@400;700&family=Carlito:wght@400;700&family=Gelasio:wght@400;700&display=swap">
<style>
:root{
  --sky-top:#0a66c8;
  --sky-bottom:#1fa8e0;
  --page:#ffffff;
  --header:#ebebeb;
  --red:#e30613;
  --red-dark:#c4000c;
  --charcoal:#434343;
  --ink:#222222;
  --text:#555555;
  --link:#2a67b1;
  --more:#1aa3e0;
  --blog-head:#7a7a7a;
  --line:#dcdcdc;
  --cyan:#33c1d8;
  --cyan-edge:#7fd9e8;
  --orange:#ff4a12;
  --green:#5bbf1c;
  --logo-grey:#8a8a8a;
}
*{box-sizing:border-box;margin:0;padding:0}
html,body{width:1001px;height:1200px;overflow:hidden}
body{background:linear-gradient(180deg,var(--sky-top),var(--sky-bottom));font-family:"Arimo",Arial,sans-serif;position:relative}
.page{position:absolute;left:119px;top:0;width:775px;height:1200px;background:var(--page)}
.header{position:absolute;left:0;top:0;width:775px;height:132px;background:var(--header)}
.abs{position:absolute}
.brand{left:36px;top:26px;display:flex;align-items:center;gap:10px}
.brand-mark{width:34px;height:34px;background:var(--logo-grey)}
.brand-name{font-family:"Carlito",sans-serif;font-size:32px;color:var(--red);font-weight:400;letter-spacing:.3px;white-space:nowrap}
.search{left:531px;top:28px;width:236px;height:34px;background:#1d5fb7;border-radius:4px;padding:4px}
.search-field{position:absolute;left:5px;top:5px;width:170px;height:24px;background:#fff;border-radius:2px;font-size:12px;color:#777;padding:6px 0 0 25px}
.search-field svg{position:absolute;left:7px;top:6px}
.search-btn{position:absolute;left:177px;top:5px;width:54px;height:24px;background:linear-gradient(#8ddb3b,var(--green));color:#fff;font-size:11px;font-weight:700;text-align:center;line-height:24px;border-radius:2px}
.nav{left:8px;top:99px;width:759px;height:30px;background:linear-gradient(#f01b22,var(--red-dark));border-radius:4px;display:flex;overflow:hidden}
.nav a{font-family:"Carlito",sans-serif;font-size:15.5px;color:#fff;text-decoration:none;line-height:30px;text-align:center;white-space:nowrap;overflow:hidden;border-right:1px solid #f6585e;flex:none}
.nav a.current{background:var(--charcoal);border:none}
.nav a:last-child{border:none}
.slider{left:11px;top:152px;width:758px;height:220px;background:linear-gradient(120deg,#0d2f55 0%,#2b6fa8 35%,#9cc9ee 52%,#3f86bc 70%,#0f3a62 100%)}
.caption{left:564px;top:78px;width:194px;height:40px;background:var(--red);color:#fff;font-family:"Gelasio",serif;font-size:13.5px;line-height:15px;padding:5px 0 0 14px;white-space:nowrap;overflow:hidden}
.caption-arrow{left:552px;top:86px;width:0;height:0;border:12px solid transparent;border-right-color:var(--red);border-left:0}
.pager{right:5px;bottom:4px;display:flex;gap:3px}
.pager span{width:18px;height:18px;background:#e4e4e4;font-size:14px;color:#111;text-align:center;line-height:18px}
.pager span.on{background:#000;color:#fff}
.section-title{font-family:"Carlito",sans-serif;font-weight:700;font-size:16.5px;color:var(--red)}
.service{width:241px;height:127px;background:linear-gradient(#fff,#e6e6e6)}
.service h3{position:absolute;left:8px;top:11px;font-family:"Gelasio",serif;font-weight:400;font-size:15px;color:var(--ink);white-space:nowrap}
.thumb{position:absolute;left:7px;top:37px;width:70px;height:70px;border:1px solid #ccc;padding:2px;background:#fff}
.thumb div{width:100%;height:100%}
.service p{position:absolute;left:84px;top:36px;width:150px;font-size:10.2px;line-height:12.7px;color:var(--text)}
.more{position:absolute;right:7px;bottom:9px;width:37px;height:14px;background:var(--more);color:#fff;font-size:10px;font-weight:700;text-align:center;line-height:14px}
.news-item{width:490px;height:60px}
.news-item .pic{position:absolute;left:0;top:0;width:52px;height:52px;border:1px solid #ddd;padding:2px;background:#fff}
.news-item .pic div{width:100%;height:100%}
.news-item h4{position:absolute;left:60px;top:-2px;font-size:11px;color:var(--link);font-weight:700}
.news-item p{position:absolute;left:60px;top:12px;width:432px;font-size:10px;line-height:12.6px;color:var(--text)}
.divider{left:515px;top:390px;width:1px;height:680px;background:var(--line)}
.blog{left:530px;top:391px;width:237px;height:287px;border:1px solid var(--line)}
.blog-head{height:36px;background:var(--blog-head);color:#fff;font-family:"Gelasio",serif;font-size:18px;line-height:36px;padding-left:12px}
.blog-item{height:62.5px;border-bottom:1px solid var(--line);padding:10px 8px 0 12px}
.blog-item:last-child{border:none}
.blog-item h5{font-size:11px;color:#111;font-weight:700;margin-bottom:2px}
.blog-item p{font-size:9.6px;line-height:12.5px;color:var(--text)}
.newsletter{left:530px;top:694px;width:237px;height:144px;background:var(--cyan);border:2px solid var(--cyan-edge);padding:8px 8px 8px 10px;color:#fff}
.newsletter h3{font-family:"Gelasio",serif;font-weight:400;font-size:18px;line-height:20px}
.newsletter p{font-size:9.6px;line-height:12.5px;margin-top:2px}
.newsletter label{display:block;font-size:11px;margin-top:6px}
.newsletter .field{width:214px;height:22px;background:#fff;margin-top:1px}
.newsletter .subscribe{width:214px;height:24px;margin-top:7px;background:linear-gradient(#ff6a2a,var(--orange));font-family:"Gelasio",serif;font-size:17px;text-align:center;line-height:24px;border:1px solid #e33a00;white-space:nowrap}
.video{left:530px;top:853px;width:237px;height:174px;background:linear-gradient(135deg,#0c3a66,#1f6aa0 55%,#0d4576)}
.video-bar{position:absolute;left:0;bottom:0;width:237px;height:12px;background:linear-gradient(#eee,#bbb);font-size:7px;line-height:12px;color:#111;white-space:nowrap}
.footer{left:8px;top:1087px;width:759px;height:103px;background:linear-gradient(#f00a12,#d9000b);border-radius:4px;color:#fff;font-family:"Carlito",sans-serif}
.footer h6{font-size:11px;font-weight:700;position:absolute;top:16px;white-space:nowrap}
.footer .col{position:absolute;font-size:9.5px;line-height:13px;white-space:nowrap}
.footer .sep{position:absolute;top:10px;width:1px;height:83px;background:#ff5a60}
.sub-form{left:576px;top:41px;width:167px;height:21px;display:flex}
.sub-form .in{flex:1;background:#fff;color:#333;font-size:9px;line-height:21px;padding-left:6px;font-family:"Arimo",sans-serif;white-space:nowrap}
.sub-form .go{width:50px;background:#222;font-size:9.5px;text-align:center;line-height:21px}
.social{position:absolute;top:69px;font-size:9.5px;display:flex;align-items:center;gap:4px;white-space:nowrap}
.social i{width:12px;height:12px;background:#fff;display:inline-block}
</style>
</head>
<body>
<div class="page">
  <header class="header">
    <div class="abs brand"><span class="brand-mark"></span><span class="brand-name">lumivane</span></div>
    <div class="abs search">
      <div class="search-field"><svg width="11" height="11" viewBox="0 0 11 11"><circle cx="4.5" cy="4.5" r="3.5" fill="none" stroke="#888" stroke-width="1.5"/><line x1="7" y1="7" x2="10.5" y2="10.5" stroke="#888" stroke-width="1.8"/></svg>Search</div>
      <div class="search-btn">SEARCH</div>
    </div>
    <nav class="abs nav">
      <a class="current" href="#" style="width:72px">Home</a><a href="#" style="width:77px">Empresa</a><a href="#" style="width:154px">Business Intelligence</a><a href="#" style="width:248px">Aplicaciones Empresariales Móviles</a><a href="#" style="width:104px">Metodología</a><a href="#" style="width:104px">Contact Us</a>
    </nav>
  </header>

  <section class="abs slider" role="img" aria-label="Glass office towers rising into a blue cloudy sky">
    <div class="abs caption-arrow"></div>
    <div class="abs caption">Lorem ipsum dolor sit amet,<br>consectetur adipisic ing elit</div>
    <div class="abs pager"><span class="on">1</span><span>2</span><span>3</span><span>4</span></div>
  </section>

  <h2 class="abs section-title" style="left:11px;top:384px">SERVICES</h2>
  <div class="abs service" style="left:11px;top:410px"><h3>Lorem ipsum dolor</h3><div class="thumb"><div role="img" aria-label="Magnifying glass over the word value" style="background:radial-gradient(#f2f2f2 40%,#6a7078)"></div></div><p>Lorem ipsum dolor sit amet, consectetur adipisicing elit, sed do eiusmod tempor incididunt ut labore et dolore magna aliqua.</p><span class="more">More</span></div>
  <div class="abs service" style="left:260px;top:410px"><h3>Lorem ipsum dolor</h3><div class="thumb"><div role="img" aria-label="Business suit holding a rising bar chart" style="background:linear-gradient(#3a3a3a,#8a8a8a)"></div></div><p>Lorem ipsum dolor sit amet, consectetur adipisicing elit, sed do eiusmod tempor incididunt ut labore et dolore magna aliqua.</p><span class="more">More</span></div>
  <div class="abs service" style="left:11px;top:542px"><h3>Lorem ipsum dolor</h3><div class="thumb"><div role="img" aria-label="Hand-drawn success flow sketch" style="background:#f4f4f4"></div></div><p>Lorem ipsum dolor sit amet, consectetur adipisicing elit, sed do eiusmod tempor incididunt ut labore et dolore magna aliqua.</p><span class="more">More</span></div>
  <div class="abs service" style="left:260px;top:542px"><h3>Lorem ipsum dolor</h3><div class="thumb"><div role="img" aria-label="Puzzle pieces over a sky and green field" style="background:linear-gradient(#3f8fe0,#9fd0f0 60%,#6cb43a)"></div></div><p>Lorem ipsum dolor sit amet, consectetur adipisicing elit, sed do eiusmod tempor incididunt ut labore et dolore magna aliqua.</p><span class="more">More</span></div>
  <div class="abs service" style="left:11px;top:675px"><h3>Lorem ipsum dolor</h3><div class="thumb"><div role="img" aria-label="Open hands holding a glowing sketch" style="background:linear-gradient(#1b2a3a,#0c1520)"></div></div><p>Lorem ipsum dolor sit amet, consectetur adipisicing elit, sed do eiusmod tempor incididunt ut labore et dolore magna aliqua.</p><span class="more">More</span></div>
  <div class="abs service" style="left:260px;top:675px"><h3>Lorem ipsum dolor</h3><div class="thumb"><div role="img" aria-label="White maze with a red path" style="background:linear-gradient(#fafafa,#e2e2e2)"></div></div><p>Lorem ipsum dolor sit amet, consectetur adipisicing elit, sed do eiusmod tempor incididunt ut labore et dolore magna aliqua.</p><span class="more">More</span></div>

  <h2 class="abs section-title" style="left:11px;top:819px">NEWS</h2>
  <article class="abs news-item" style="left:11px;top:853px"><div class="pic"><div role="img" aria-label="Small figures in a network" style="background:#eef2f5"></div></div><h4>Heading</h4><p>Lorem ipsum dolor sit amet, consectetur adipisicing elit, sed do eiusmod tempor incididunt ut labore et dolore magna aliqua. Ut enim ad minim veniam, quis nostrud exercitation ullamco laboris nisi ut aliquip ex ea commodo consequat.</p></article>
  <article class="abs news-item" style="left:11px;top:928px"><div class="pic"><div role="img" aria-label="Darts hitting a red target" style="background:radial-gradient(#e23a3a 25%,#f4f4f4 60%)"></div></div><h4>Heading</h4><p>Lorem ipsum dolor sit amet, consectetur adipisicing elit, sed do eiusmod tempor incididunt ut labore et dolore magna aliqua. Ut enim ad minim veniam, quis nostrud exercitation ullamco laboris nisi ut aliquip ex ea commodo consequat.</p></article>
  <article class="abs news-item" style="left:11px;top:1003px"><div class="pic"><div role="img" aria-label="Sunlight through green leaves" style="background:radial-gradient(#fff6b0 15%,#c8b820 45%,#3d6b1e)"></div></div><h4>Heading</h4><p>Lorem ipsum dolor sit amet, consectetur adipisicing elit, sed do eiusmod tempor incididunt ut labore et dolore magna aliqua. Ut enim ad minim veniam, quis nostrud exercitation ullamco laboris nisi ut aliquip ex ea commodo consequat.</p></article>

  <div class="abs divider"></div>

  <aside class="abs blog">
    <div class="blog-head">BLOG</div>
    <div class="blog-item"><h5>Blog title</h5><p>Lorem ipsum dolor sit amet, consectetur adipisic ing elit, sed do eiusmod tempor.</p></div>
    <div class="blog-item"><h5>Blog title</h5><p>Lorem ipsum dolor sit amet, consectetur adipisic ing elit, sed do eiusmod tempor.</p></div>
    <div class="blog-item"><h5>Blog title</h5><p>Lorem ipsum dolor sit amet, consectetur adipisic ing elit, sed do eiusmod tempor.</p></div>
    <div class="blog-item"><h5>Blog title</h5><p>Lorem ipsum dolor sit amet, consectetur adipisic ing elit, sed do eiusmod tempor.</p></div>
  </aside>

  <aside class="abs newsletter">
    <h3>NEWSLETTER</h3>
    <p>Lorem ipsum dolor sit amet, consectetur adipisic ing elit, sed do eiusmod tempor.</p>
    <label>Email Address</label>
    <div class="field"></div>
    <div class="subscribe">SUBSCRIBE NOW</div>
  </aside>

  <div class="abs video" role="img" aria-label="Video still of abstract arrows and rising bars">
    <svg class="abs" style="left:108px;top:70px" width="16" height="18" viewBox="0 0 16 18"><polygon points="2,1 15,9 2,17" fill="#9fc4e2"/></svg>
    <div class="video-bar">&nbsp;▶ &nbsp;00:00 <span style="display:inline-block;width:125px;height:3px;background:#777;vertical-align:middle"></span> 00:00</div>
  </div>

  <footer class="abs footer">
    <h6 style="left:15px">© 2011 lumivane</h6>
    <div class="col" style="left:15px;top:56px">All right are reserved.<br>Terms of service &nbsp;|&nbsp; Privacy Policy</div>
    <div class="sep" style="left:160px"></div>
    <h6 style="left:174px">Contact Info</h6>
    <div class="col" style="left:174px;top:42px">123 Lorem ipsum dolor<br>Some City, P.O 54898<br>T: +00 1254 5874</div>
    <div class="sep" style="left:286px"></div>
    <h6 style="left:301px">Quick Navigation</h6>
    <div class="col" style="left:304px;top:42px">Home<br>Empresa<br>Business Intelligence</div>
    <div class="col" style="left:404px;top:42px">Aplicaciones empresariales móviles<br>Metodología<br>Contact Us</div>
    <div class="sep" style="left:563px"></div>
    <h6 style="left:574px">Connect with us</h6>
    <div class="abs sub-form"><span class="in">Subscribe to newsletter</span><span class="go">Submit</span></div>
    <div class="social" style="left:576px"><i></i>Join Us on Circlenet</div>
    <div class="social" style="left:693px"><i></i>Chirpline</div>
  </footer>
</div>
</body>
</html>
```